Publisher needs a book cover design for ‘Lanterns Over the Marsh Gate’ book

We need a book cover (front, back, spine) for the 2nd edition of a book entitled ‘Lanterns Over the Marsh Gate’ and subtitled ‘the quiet geography of tidal winds, ferry routes and harbour lanterns’ (inverted commas not to be part of the title and subtitle). The author is Rupert Calloway. The publisher is Vellmark Press. The finished size of the paperback version will be the industry standard 9" x 6". There will be paperback, hardback, and e-book versions. The final number of pages is expected to be in the region 150-180 pages. Text for the back cover is not yet available, but at the bottom of the back cover should be publisher logo (rectangular) on the left and space for the ISBN bar code on the right. The circular logo should be on the spine. The design should be original and not include any stock images that have been created by someone else or may require obtaining a copyright licence to use. Symbols in common use and not copyrighted are probably ok. There are no required images, photographs or symbols except the publisher logo at the left bottom of the back cover and lower spine. Spine lettering should be UK/US style with the top of the writing nearest the front cover. The designer is free to be creative using appropriate diagrams, symbols or abstract designs. Rectangular and circular variants of the publisher logo are attached. Designers are assured that when evaluating designs absolutely no notice whatsoever is taken of a designer's Pixo Rally ranking or status; We are completely output driven, so what matters is the design, not the ranking or status of the designer. In a similar way, designs are not evaluated as 'good' or 'bad' - the winning design will be chosen after review by a design review panel and is not decided arbitrarily by a single person. All submitted designs should be capable of effective copyright assignment.

Target Market(s)

Practitioners, parents, teachers, pupils and academics concerned with child protection, safeguarding and the elimination of emotional abuse of children in the classroom

Font styles to use
Serif
Sans Serif

Requirements
Must have
• • Title, author, edition, subtitle, publisher logo
Nice to have
• • Originality, innovation
Should not have
• • Stock images or anything else requiring additional copyright discussions and negotiations.

```html
<!DOCTYPE html>
<html lang="en">
<head>
<meta charset="utf-8">
<title>Lanterns Over the Marsh Gate — Cover Spread</title>
<link rel="stylesheet" href="https://fonts.googleapis.com/css2?family=Oswald:wght@600&family=Tinos:wght@400;700&family=Montserrat:wght@500&display=swap">
<style>
  :root {
    --backdrop: #b8b8b8;
    --paper: #ffffff;
    --paper-edge: #e6e6e6;
    --signal-red: #f20a0a;
    --spine-red: #e00808;
    --ink: #111111;
    --type-on-red: #ffffff;
    --font-title: "Oswald", sans-serif;
    --font-serif: "Tinos", serif;
    --font-label: "Montserrat", sans-serif;
  }
  * { box-sizing: border-box; margin: 0; padding: 0; }
  html, body { width: 1200px; height: 800px; overflow: hidden; }
  body { background: var(--backdrop); position: relative; }

  .cover-spread {
    position: absolute; left: 135px; top: 70px;
    width: 930px; height: 660px;
    display: flex;
    box-shadow: 0 10px 30px rgba(0,0,0,0.25);
  }
  .panel { position: relative; width: 440px; height: 660px; background: var(--signal-red); overflow: hidden; }
  .torn-paper { position: absolute; inset: 0; width: 100%; height: 100%; }
  .torn-paper .sheet { fill: var(--paper); }
  .torn-paper .sheet-edge { fill: var(--paper-edge); }

  /* Back cover */
  .back-copy {
    position: absolute; left: 58px; top: 150px; width: 330px;
    font-family: var(--font-serif); color: var(--type-on-red);
    font-size: 11.4px; line-height: 1.32; text-align: justify; hyphens: auto;
  }
  .back-copy h2 { font-weight: 400; font-size: 19px; margin: 16px 0 6px; }
  .imprint {
    position: absolute; left: 40px; bottom: 36px;
    display: flex; align-items: center; gap: 8px;
    font-family: var(--font-serif); font-size: 20px; color: var(--ink); letter-spacing: 0.5px;
  }
  .imprint-dot { width: 24px; height: 24px; border-radius: 50%; background: var(--ink); }

  /* Spine */
  .spine { position: relative; width: 50px; height: 660px; background: var(--spine-red); overflow: hidden; }
  .spine-cap { position: absolute; left: 0; width: 50px; background: var(--paper); }
  .spine-cap.top { top: 0; height: 150px; }
  .spine-cap.bottom { bottom: 0; height: 80px; }
  .spine-edition {
    position: absolute; top: 18px; left: 50%; transform: translateX(-50%);
    writing-mode: vertical-rl; font-family: var(--font-label); font-size: 12px;
    letter-spacing: 2px; color: var(--ink);
  }
  .spine-line {
    position: absolute; top: 168px; left: 50%; transform: translateX(-50%);
    writing-mode: vertical-rl; white-space: nowrap; color: var(--type-on-red);
    display: flex; align-items: center; gap: 14px;
  }
  .spine-title { font-family: var(--font-title); font-size: 17px; letter-spacing: 0.5px; text-transform: uppercase; }
  .spine-author { font-family: var(--font-serif); font-weight: 700; font-size: 13px; letter-spacing: 1px; text-transform: uppercase; }
  .spine-imprint {
    position: absolute; bottom: 14px; left: 0; width: 50px;
    display: flex; flex-direction: column; align-items: center; gap: 4px;
    font-family: var(--font-serif); font-size: 6.5px; color: var(--ink); text-align: center; line-height: 1.1;
  }
  .spine-imprint .imprint-dot { width: 20px; height: 20px; }

  /* Front cover */
  .front-edition {
    position: absolute; top: 52px; left: 0; width: 100%; text-align: center;
    font-family: var(--font-label); font-size: 24px; letter-spacing: 4px; color: var(--ink);
  }
  .front-title {
    position: absolute; top: 196px; left: 0; width: 100%; text-align: center;
    font-family: var(--font-title); font-weight: 600; font-size: 78px; line-height: 0.98;
    color: var(--type-on-red); text-transform: uppercase; letter-spacing: 1px;
  }
  .front-subtitle {
    position: absolute; top: 450px; left: 50px; width: 340px; text-align: center;
    font-family: var(--font-serif); font-size: 13.5px; line-height: 1.3; letter-spacing: 1px;
    color: var(--type-on-red); text-transform: uppercase;
  }
  .front-author {
    position: absolute; bottom: 28px; left: 0; width: 100%; text-align: center;
    font-family: var(--font-serif); font-weight: 700; font-size: 31px; letter-spacing: 2px;
    color: var(--ink); text-transform: uppercase;
  }
</style>
</head>
<body>
  <main class="cover-spread">

    <section class="panel back-cover">
      <svg class="torn-paper" viewBox="0 0 440 660" preserveAspectRatio="none" aria-hidden="true">
        <path class="sheet-edge" d="M0 0H440V99L420 92L400 104L385 96L360 114L340 99L320 104L300 84L280 94L255 74L235 89L215 82L190 99L170 90L150 104L130 102L110 119L85 112L60 122L40 114L20 126L0 119Z"/>
        <path class="sheet" d="M0 0H440V95L420 88L400 100L385 92L360 110L340 95L320 100L300 80L280 90L255 70L235 85L215 78L190 95L170 86L150 100L130 98L110 115L85 108L60 118L40 110L20 122L0 115Z"/>
        <path class="sheet-edge" d="M0 660V586L20 571L45 581L70 556L95 566L120 541L140 556L165 544L190 561L215 548L240 566L265 556L290 571L315 561L340 581L365 571L390 586L415 576L440 588V660Z"/>
        <path class="sheet" d="M0 660V590L20 575L45 585L70 560L95 570L120 545L140 560L165 548L190 565L215 552L240 570L265 560L290 575L315 565L340 585L365 575L390 590L415 580L440 592V660Z"/>
      </svg>
      <div class="back-copy">
        <p>We need a book cover (front, back, spine) for the 2nd edition of a book entitled ‘Lanterns Over the Marsh Gate’ and subtitled ‘the quiet geography of tidal winds, ferry routes and harbour lanterns’ (inverted commas not to be part of the title and subtitle). The author is Rupert Calloway. The publisher is Vellmark Press. The finished size of the paperback version will be the industry standard 9" x 6". There will be paperback, hardback, and e-book versions. The final number of pages is expected to be in the region 150-180 pages. Text for the back cover is not yet available, but at the bottom of the back cover should be publisher logo (rectangular) on the left and space for the ISBN bar code on the right. The circular logo should be on the spine.</p>
        <h2>Author Biography</h2>
        <p>Spine lettering should be UK/US style with the top of the writing nearest the front cover. The designer is free to be creative using appropriate diagrams, symbols or abstract designs. Rectangular and circular variants of the publisher logo are attached. Designers are assured that when evaluating designs absolutely no notice whatsoever is taken of a designer's Pixo Rally ranking or status; We are completely output driven, so what matters is the design, not the ranking or status of the designer.</p>
      </div>
      <div class="imprint">
        <span class="imprint-dot"></span>
        <span class="imprint-name">VELLMARK PRESS</span>
      </div>
    </section>

    <section class="spine">
      <div class="spine-cap top"></div>
      <div class="spine-cap bottom"></div>
      <span class="spine-edition">2ND EDITION</span>
      <div class="spine-line">
        <span class="spine-title">Lanterns Over the Marsh Gate</span>
        <span class="spine-author">Rupert Calloway</span>
      </div>
      <div class="spine-imprint">
        <span class="imprint-dot"></span>
        <span>VELLMARK<br>PRESS</span>
      </div>
    </section>

    <section class="panel front-cover">
      <svg class="torn-paper" viewBox="0 0 440 660" preserveAspectRatio="none" aria-hidden="true">
        <path class="sheet-edge" d="M0 0H440V109L420 104L400 122L380 116L360 139L340 134L320 152L300 146L280 164L260 151L240 170L220 160L200 178L180 166L160 183L140 170L110 186L80 176L50 188L25 180L0 193Z"/>
        <path class="sheet" d="M0 0H440V105L420 100L400 118L380 112L360 135L340 130L320 148L300 142L280 160L260 147L240 166L220 156L200 174L180 162L160 179L140 166L110 182L80 172L50 184L25 176L0 189Z"/>
        <path class="sheet-edge" d="M0 660V596L30 588L60 594L90 572L120 576L150 558L180 564L210 540L240 548L270 530L300 536L330 514L360 521L390 504L415 510L440 496V660Z"/>
        <path class="sheet" d="M0 660V600L30 592L60 598L90 576L120 580L150 562L180 568L210 544L240 552L270 534L300 540L330 518L360 525L390 508L415 514L440 500V660Z"/>
      </svg>
      <p class="front-edition">2ND EDITION</p>
      <h1 class="front-title">Lanterns<br>Over the<br>Marsh Gate</h1>
      <p class="front-subtitle">The quiet geography of tidal winds, ferry routes and harbour lanterns</p>
      <p class="front-author">Rupert Calloway</p>
    </section>

  </main>
</body>
</html>
```